Product Marketing Slick / Product Brief. 1 sheet now then an additional 2 plus more in the future.

We need to create 1 page product sheets that will be used for marketing purposes.
The products we are selling are network security and network compliance for PCI, HIPAA and GDPR.
We will essentially be doing all of the consulting to make their networks secure, then on a daily basis be scanning and validating that all of the government requirements are being met for compliance.
We dont want to make this too technical so its more of a page that will discuss in general terms what we do and why its important for them to have our services.
***Note There will be a total of Three Sheets, this project is for the first one and can be for any one of the products. HIPAA Compliance , PCI Compliance or GDPR Compliance.
We will contract with you to do the additional 2 pages and probably more if we select your design.
Target Market(s)
Medical, Hospitality
Industry/Entity Type
Medical
Colors
Designer to choose colors to be used in the design.

```html
<!DOCTYPE html>
<html lang="en">
<head>
<meta charset="utf-8">
<title>Clearvance – Compliance Product Sheet</title>
<link rel="stylesheet" href="https://fonts.googleapis.com/css2?family=Arimo:ital,wght@0,400;1,700&family=Bebas+Neue&family=Montserrat:wght@400;500&display=swap">
<style>
  :root{
    --navy:#1f4a7e;
    --green:#9cbd72;
    --green-light:#b3cf8d;
    --ink:#4a4a4a;
    --muted:#7b8a99;
    --white:#ffffff;
    --backdrop:#c4c4c4;
    --shade:rgba(40,32,28,.82);
  }
  *{box-sizing:border-box;margin:0;padding:0}
  html,body{width:1200px;height:669px;overflow:hidden;background:var(--backdrop)}
  .sheet{
    position:absolute;left:376px;top:19px;width:515px;height:725px;
    transform:scale(.87);transform-origin:0 0;
    background:var(--white);overflow:hidden;
    box-shadow:0 10px 24px rgba(0,0,0,.25);
    font-family:"Arimo",Arial,sans-serif;color:var(--ink);
  }
  .hero-photo{
    position:absolute;left:0;top:60px;width:515px;height:360px;
    background:linear-gradient(135deg,#5a3a26 0%,#9a6a45 30%,#d9d3cc 55%,#c9c2ba 75%,#7a5a45 100%);
  }
  .header-waves{position:absolute;left:0;top:0;width:515px;height:160px}
  .brand{position:absolute;left:16px;top:22px;display:flex;align-items:center;gap:7px}
  .brand-mark{width:22px;height:22px;border-radius:50%;background:var(--green)}
  .brand-name{font-family:"Montserrat",sans-serif;font-weight:500;font-size:15px;letter-spacing:2px;color:var(--navy)}
  .brand-tagline{position:absolute;left:72px;top:42px;font-size:7px;color:var(--muted);font-family:"Arimo",Arial,sans-serif}
  .headline{position:absolute;left:0;font-family:"Bebas Neue",sans-serif;color:var(--white);
    background:var(--shade);font-size:31px;line-height:1;padding:7px 10px 4px 18px;letter-spacing:.5px}
  .headline.line-1{top:180px}
  .headline.line-2{top:224px}
  .service{position:absolute;top:385px;width:146px;height:126px;background:var(--navy);
    text-align:center;color:var(--white);font-family:"Montserrat",sans-serif}
  .service.hipaa{left:24px}.service.pci{left:184px}.service.gdpr{left:344px}
  .service-name{position:absolute;left:0;right:0;top:72px;font-size:24px;font-weight:500;line-height:1}
  .service-sub{position:absolute;left:0;right:0;top:97px;font-size:15px;letter-spacing:.3px}
  .service-badge{position:absolute;top:318px;width:124px;height:124px;border-radius:50%;
    background:var(--green);border:4px solid var(--white)}
  .service-badge.hipaa{left:35px}.service-badge.pci{left:195px}.service-badge.gdpr{left:355px}
  .divider{position:absolute;left:0;top:511px;width:515px;height:9px;background:var(--green-light)}
  .copy{position:absolute;top:540px;width:232px;font-size:9px;line-height:13px;text-align:justify}
  .copy.left{left:13px}.copy.right{left:273px}
  .copy p+p{margin-top:13px}
  .callout{position:absolute;left:0;top:652px;width:515px;height:34px}
  .callout-text{position:absolute;left:0;top:656px;width:515px;text-align:center;color:var(--white);
    font-size:9.5px;font-style:italic;font-weight:700;line-height:13px}
  .footer{position:absolute;left:0;top:688px;width:515px;height:22px;background:var(--navy);
    color:var(--white);font-size:8.5px;display:flex;align-items:center;justify-content:space-between;padding:0 22px 0 30px}
  .footer-item{display:flex;align-items:center;gap:7px}
  .footer-item svg{width:12px;height:12px}
  .base-strip{position:absolute;left:0;top:710px;width:515px;height:15px;background:var(--green-light)}
</style>
</head>
<body>
<main class="sheet">
  <div class="hero-photo" role="img" aria-label="Photo of hands typing on a laptop keyboard at a wooden desk"></div>

  <svg class="header-waves" viewBox="0 0 515 160" aria-hidden="true">
    <path d="M0 0H515V18C430 28 330 40 250 62C160 86 80 104 0 108Z" fill="var(--navy)"/>
    <path d="M0 0H515V14C420 20 320 36 230 58C150 78 70 92 0 96Z" fill="var(--white)"/>
    <path d="M0 96C70 92 150 78 230 58C320 36 420 20 515 14V34C430 40 330 56 250 78C160 102 80 112 0 112Z" fill="var(--navy)"/>
    <path d="M250 100C340 70 430 50 515 46V72C440 72 360 86 280 104C250 110 220 112 200 112C215 108 232 104 250 100Z" fill="var(--green)"/>
  </svg>

  <div class="brand"><span class="brand-mark"></span><span class="brand-name">CLEARVANCE</span></div>
  <div class="brand-tagline">network security made simple</div>

  <div class="headline line-1">SMART, SIMPLE, SAFE, SECURE</div>
  <div class="headline line-2">WE WORRY, SO YOU DON'T HAVE TO</div>

  <section class="service hipaa"><div class="service-name">HIPAA</div><div class="service-sub">COMPLIANCE</div></section>
  <section class="service pci"><div class="service-name">PCI</div><div class="service-sub">COMPLIANCE</div></section>
  <section class="service gdpr"><div class="service-name">GDPR</div><div class="service-sub">COMPLIANCE</div></section>

  <div class="service-badge hipaa" role="img" aria-label="HIPAA service icon"></div>
  <div class="service-badge pci" role="img" aria-label="PCI service icon"></div>
  <div class="service-badge gdpr" role="img" aria-label="GDPR service icon"></div>

  <div class="divider"></div>

  <div class="copy left">
    <p>Clearvance has been securing networks for over twenty years &amp; was one of the first managed security companies in the country. Thousands of satisfied &amp; secured customers can't be wrong. There's a reason for our longevity &amp; we want to pass that on to you. As the times &amp; threats have changed so have we, adapting &amp; overcoming each new menace that arises, staying at the forefront of technology so we can keep you safe.</p>
  </div>
  <div class="copy right">
    <p>Compliance is a key component not only to keeping your safe &amp; secure but also to ensure your organization is up to speed on all new government regulations &amp; requirements.</p>
    <p>Do you really want to know all the complexities of HIPAA &amp; PCI compliance? Yes? We'll teach you everything you need to know.</p>
  </div>

  <svg class="callout" viewBox="0 0 515 34" aria-hidden="true">
    <path d="M70 0H445L470 34H45Z" fill="var(--green)"/>
  </svg>
  <div class="callout-text">No? We'll handle everything from start to finish and manage and maintain<br>it so you never have to think or worry about it again.</div>

  <footer class="footer">
    <span class="footer-item">
      <svg viewBox="0 0 12 12" aria-hidden="true"><circle cx="6" cy="6" r="6" fill="var(--white)"/><path d="M6 2.5a2.2 2.2 0 0 1 2.2 2.2C8.2 6.5 6 9.5 6 9.5S3.8 6.5 3.8 4.7A2.2 2.2 0 0 1 6 2.5Z" fill="var(--navy)"/></svg>
      Lorem ipsum text, USA, Lane 5</span>
    <span class="footer-item">
      <svg viewBox="0 0 12 12" aria-hidden="true"><circle cx="6" cy="6" r="6" fill="var(--white)"/><path d="M3.8 3l1.3-.3.7 1.6-.8.6a4.5 4.5 0 0 0 2 2l.6-.8 1.6.7L8.9 8A5.5 5.5 0 0 1 3.8 3Z" fill="var(--navy)"/></svg>
      91 - 55501 - 24680</span>
    <span class="footer-item">
      <svg viewBox="0 0 12 12" aria-hidden="true"><circle cx="6" cy="6" r="6" fill="var(--white)"/><rect x="3" y="4" width="6" height="4.2" fill="var(--navy)"/><path d="M3 4l3 2.3L9 4" fill="none" stroke="var(--white)" stroke-width=".7"/></svg>
      info@clearvance.net</span>
  </footer>
  <div class="base-strip"></div>
</main>
</body>
</html>
```